Business Card design for Recruiter providing Recruitment Staff Augmentation services

I need a double sided business card. I have used Plix to print cards in the past and really like their quality. I have a logo but need to change the tagline that is part of the graphic.

The tagline currently reads and Connnecting people with careers - but it should be removed.

The back should look like a notecard for writing a to do list with the first to-do Augment Recruiting Staff

```html
<!DOCTYPE html>
<html lang="en">
<head>
<meta charset="utf-8">
<title>Talent Summit – Business Card</title>
<link rel="stylesheet" href="https://fonts.googleapis.com/css2?family=Lexend:wght@400&family=Source+Sans+3:wght@400;600&display=swap">
<style>
  :root {
    --backdrop: #141414;
    --card: #ffffff;
    --navy: #0d3a5c;
    --accent: #d2492a;
    --rule: #a9b9c6;
    --ink: #1f2a33;
  }
  * { margin: 0; padding: 0; box-sizing: border-box; }
  html, body { width: 1200px; height: 900px; overflow: hidden; }
  body { background: var(--backdrop); position: relative; font-family: "Source Sans 3", sans-serif; }

  .card {
    position: absolute;
    top: 306px;
    width: 439px;
    height: 271px;
    background: var(--card);
    border-radius: 10px;
    overflow: hidden;
  }
  .card--front { left: 149px; }
  .card--back { left: 609px; }

  .brand-name {
    position: absolute;
    left: 34px;
    top: 54px;
    font-family: "Lexend", sans-serif;
    font-weight: 400;
    font-size: 34px;
    letter-spacing: 1px;
    color: var(--navy);
    white-space: nowrap;
  }

  .holder-name {
    position: absolute;
    left: 28px;
    top: 145px;
    font-weight: 600;
    font-size: 15px;
    color: var(--navy);
  }
  .holder-rule {
    position: absolute;
    left: 28px;
    top: 182px;
    width: 342px;
    height: 1px;
    background: var(--rule);
  }
  .contact-list {
    position: absolute;
    left: 28px;
    top: 197px;
    list-style: none;
    font-size: 12px;
    line-height: 16px;
    color: var(--ink);
  }
  .contact-list li { display: flex; align-items: center; gap: 7px; }
  .contact-icon { width: 9px; height: 9px; fill: var(--navy); }

  .corner-swoosh { position: absolute; inset: 0; width: 100%; height: 100%; }

  .note-lines { position: absolute; inset: 0; width: 100%; height: 100%; }
</style>
</head>
<body>

  <section class="card card--front" aria-label="Business card front">
    <div class="brand-name">TALENT SUMMIT</div>

    <div class="holder-name">Dana Whitfield,SPHR</div>
    <div class="holder-rule"></div>

    <ul class="contact-list">
      <li>
        <svg class="contact-icon" viewBox="0 0 10 10" aria-hidden="true">
          <path d="M2 0.5 L3.6 2.6 L2.7 3.6 C3.3 5 4.9 6.6 6.4 7.3 L7.4 6.4 L9.5 8 L8.5 9.5 C4.5 9.3 0.7 5.5 0.5 1.5 Z"/>
        </svg>
        303-555-0142
      </li>
      <li>
        <svg class="contact-icon" viewBox="0 0 10 10" aria-hidden="true">
          <path d="M0.5 2 H9.5 V8.5 H0.5 Z M1.2 2.6 L5 5.4 L8.8 2.6" fill="var(--navy)" stroke="#fff" stroke-width="0.8"/>
        </svg>
        Dana@talentsummit.com
      </li>
    </ul>

    <svg class="corner-swoosh" viewBox="0 0 439 271" aria-hidden="true">
      <path d="M138 271 C270 255 400 215 439 128 L439 271 Z" fill="var(--accent)"/>
      <path d="M146 271 C290 260 410 220 439 152 L439 271 Z" fill="var(--navy)"/>
    </svg>
  </section>

  <section class="card card--back" aria-label="Business card back, to-do notecard">
    <svg class="note-lines" viewBox="0 0 440 271" aria-hidden="true">
      <g stroke="var(--rule)" stroke-width="1">
        <line x1="36" y1="58.5" x2="400" y2="58.5"/>
        <line x1="36" y1="111.5" x2="400" y2="111.5"/>
        <line x1="36" y1="162.5" x2="400" y2="162.5"/>
        <line x1="36" y1="215.5" x2="400" y2="215.5"/>
      </g>
    </svg>
  </section>

</body>
</html>
```